Signage for a foam car wash facility

We need signages done for a foam car wash.
We use only premium, environment-friendly, biodegradable foam wash and cleaning products.
We are in a commercial center (mall) situated in an upscale part of town and need our signage to reflect that.
We need signages for directions (two or three smaller ones), one showing that we are here, and at the actual car wash.
We will provide our logo, the texts, some pictures of the actual location the dimensions of the signages.
We need the signages to be informative, clean, crisp, modern with the use of icons if possible and some colour so that we get the attention of clients passing -by without being too flashy.
Directions to the car wash should look like a petal of a flower directing towards the car wash

Target Market(s)

Upscale market with a school and a gym next to it. Mom and dad's dropping their children at school, offices nearby.

Industry/Entity Type

Car Wash

Requirements
Nice to have
• icons, some colors,Directions to the car wash should look like a petal of a flower directing towards the car wash

```html
<!DOCTYPE html>
<html lang="en">
<head>
<meta charset="UTF-8">
<title>Foliara Foam Wash Banner</title>
<link href="https://fonts.googleapis.com/css2?family=Montserrat:wght@500;600&display=swap" rel="stylesheet">
<style>
  :root {
    --ink: #000000;
    --lime: #b3cf3c;
    --white: #ffffff;
    --leaf-dark: #3f5a36;
    --leaf-light: #8fae7f;
  }
  html, body {
    margin: 0;
    padding: 0;
    width: 1200px;
    height: 160px;
    overflow: hidden;
    background: var(--ink);
  }
  .banner {
    position: relative;
    width: 1200px;
    height: 160px;
    background: var(--ink);
    overflow: hidden;
    font-family: "Montserrat", sans-serif;
  }
  .brand {
    position: absolute;
    left: 112px;
    top: 50px;
    display: flex;
    align-items: center;
    gap: 22px;
  }
  .brand-dot {
    width: 34px;
    height: 34px;
    border-radius: 50%;
    background: var(--lime);
  }
  .brand-name {
    margin: 0;
    color: var(--lime);
    font-weight: 600;
    font-size: 46px;
    letter-spacing: 3px;
    line-height: 1;
  }
  .divider {
    position: absolute;
    left: 553px;
    top: 41px;
    width: 2px;
    height: 91px;
    background: var(--white);
  }
  .services {
    position: absolute;
    left: 601px;
    top: 38px;
    margin: 0;
    padding: 0;
    list-style: none;
  }
  .services li {
    position: relative;
    padding-left: 20px;
    color: var(--white);
    font-weight: 500;
    font-size: 19px;
    letter-spacing: 1.6px;
    line-height: 32px;
  }
  .services li::before {
    content: "";
    position: absolute;
    left: 0;
    top: 13px;
    width: 7px;
    height: 7px;
    border-radius: 50%;
    background: var(--lime);
  }
  .foam {
    position: absolute;
    right: 0;
    top: 0;
    width: 220px;
    height: 160px;
  }
  .foam-bubble {
    position: absolute;
    left: 1019px;
    top: 20px;
    width: 14px;
    height: 14px;
    border-radius: 50%;
    background: var(--lime);
  }
  .plant {
    position: absolute;
    left: 1012px;
    top: 38px;
    width: 168px;
    height: 122px;
    border-radius: 48% 48% 0 0;
    background: radial-gradient(ellipse at 55% 45%, var(--leaf-light) 0%, var(--leaf-dark) 70%, rgba(63,90,54,0) 100%);
  }
</style>
</head>
<body>
  <div class="banner">
    <div class="brand">
      <span class="brand-dot"></span>
      <h1 class="brand-name">FOLIARA</h1>
    </div>

    <div class="divider"></div>

    <ul class="services">
      <li>VACCUM CLEANER</li>
      <li>INTERIOR OF THE CARS</li>
      <li>DASHBOARDS</li>
    </ul>

    <svg class="foam" viewBox="0 0 220 160" aria-hidden="true">
      <path fill="#ffffff" d="M0 160 C2 140 14 128 28 126 C20 110 26 92 42 86 C38 66 52 50 70 50 C72 32 88 20 104 22 C114 8 134 4 150 12 C164 0 190 2 200 16 C208 12 216 12 220 14 L220 160 Z"/>
    </svg>
    <span class="foam-bubble"></span>
    <div class="plant" role="img" aria-label="Photo of green eucalyptus sprigs"></div>
  </div>
</body>
</html>
```